Formal letterhead for Commercial Real Estate Company

Formal and professional letterhead for the transactional documents of a commercial real estate company.

Elements to be Included between header and footer:

- Logo (attached)(should be applied without the yellow background, in other words, the background colour for the design should be white)
- Slogan: Your Property Solution
- Physical Address: 41 Tamsin Lane, Oakridge, Durban, 4001
- Postal Address: PO Box 72948, Kelvale, 4062
- Phone: 031 684 9152
- Fax: 031 739 4218
- Website: www.dunholt.co.zaz
- eMail: contact@dunholt.co.za

The brand guide is attached (the one you last provided), it does not provide direction on letterhead specifically but on other brand aspects.

```html
<!DOCTYPE html>
<html lang="en">
<head>
<meta charset="utf-8">
<title>Dunholt Letterhead</title>
<link rel="stylesheet" href="https://fonts.googleapis.com/css2?family=Montserrat:wght@500;800&family=Source+Sans+3:wght@400&family=Arimo:wght@700&display=swap">
<style>
  :root {
    --paper: #ffffff;
    --ink: #1c1c1c;
    --body-ink: #4a4a4a;
    --footer-ink: #3a3a3a;
    --rule-dark: #3b3b3b;
    --rule-olive: #b9b52a;
    --brand-yellow: #f2e600;
    --sig-tone: #e9e9e9;
  }
  * { box-sizing: border-box; margin: 0; padding: 0; }
  html, body { width: 950px; height: 1200px; overflow: hidden; background: var(--paper); }
  .letterhead { position: relative; width: 950px; height: 1200px; background: var(--paper); }

  .brand { position: absolute; left: 76px; top: 84px; }
  .brand-name {
    font-family: "Montserrat", sans-serif; font-weight: 800;
    font-size: 38px; letter-spacing: 1px; color: var(--ink); line-height: 1;
  }
  .brand-est {
    margin-top: 8px; font-family: "Montserrat", sans-serif; font-weight: 500;
    font-size: 10.5px; letter-spacing: 0.4px; color: var(--ink);
  }

  .salutation {
    position: absolute; left: 76px; top: 256px;
    font-family: "Arimo", sans-serif; font-weight: 700; font-size: 19px; color: #2b2b2b;
  }
  .letter-body {
    position: absolute; left: 76px; top: 303px; width: 798px;
    font-family: "Source Sans 3", sans-serif; font-size: 17.6px; line-height: 22.4px;
    color: var(--body-ink); text-align: justify;
  }
  .letter-body p + p { margin-top: 22.4px; }

  .signature { position: absolute; left: 77px; top: 885px; width: 148px; height: 66px; }

  .footer-address {
    position: absolute; left: 76px; top: 1117px;
    font-family: "Montserrat", sans-serif; font-weight: 500; font-size: 11.6px; color: var(--footer-ink);
  }
  .footer-rule { position: absolute; left: 0; top: 1133px; width: 950px; height: 4px; }
  .footer-contacts {
    position: absolute; left: 76px; top: 1141px; display: flex; gap: 14px; align-items: center;
    font-family: "Montserrat", sans-serif; font-weight: 500; font-size: 11.6px; color: var(--footer-ink);
  }
  .contact { display: flex; align-items: center; gap: 6px; }
  .contact svg { width: 10px; height: 10px; fill: var(--footer-ink); }
  .footer-mark { position: absolute; left: 818px; top: 1107px; width: 56px; height: 56px; }
</style>
</head>
<body>
<main class="letterhead">
  <header class="brand">
    <div class="brand-name">DUNHOLT</div>
    <div class="brand-est">ESTABLISHED IN 1958</div>
  </header>

  <h1 class="salutation">Dear Mr. Harlow,</h1>

  <section class="letter-body">
    <p>Lorem Ipsum is simply dummy text of the printing and typesetting industry. Lorem Ipsum has been the industry's standard dummy text ever since the 1500s, when an unknown printer took a galley of type and scrambled it to make a type specimen book. It has survived not only five centuries, but also the leap into electronic typesetting, remaining essentially unchanged.</p>
    <p>The standard chunk of Lorem Ipsum used since the 1500s is reproduced below for those interested. Sections 1.10.32 and 1.10.33 from "de Finibus Bonorum et Malorum" by Aurelan are also reproduced in their exact original form, accompanied by English versions from the 1914 translation by H. Whitcombe</p>
    <p>Lorem Ipsum is simply dummy text of the printing and typesetting industry. Lorem Ipsum has been the industry's standard dummy text ever since the 1500s, when an unknown printer took a galley of type and scrambled it to make a type specimen book. It has survived not only five centuries, but also the leap into electronic typesetting, remaining essentially unchanged. It was popularised in the</p>
    <p>The standard chunk of Lorem Ipsum used since the 1500s is reproduced below for those interested. Sections 1.10.32 and 1.10.33 from "de Finibus Bonorum et Malorum" by Aurelan are also reproduced in their exact original form, accompanied by English versions from the 1914 translation by H. Whitcombe</p>
    <p>The standard chunk of Lorem Ipsum used since the 1500s is reproduced below for those interested. Sections 1.10.32 and 1.10.33 from "de Finibus Bonorum et Malorum" by Aurelan are also reproduced in their exact original form.</p>
  </section>

  <svg class="signature" role="img" aria-label="Handwritten signature of the sender" viewBox="0 0 148 66">
    <defs>
      <linearGradient id="sigFill" x1="0" x2="1">
        <stop offset="0" stop-color="#e4e4e4"/><stop offset="1" stop-color="#f2f2f2"/>
      </linearGradient>
    </defs>
    <rect width="148" height="66" rx="6" fill="url(#sigFill)"/>
  </svg>

  <div class="footer-address">41 Tamsin Lane, Oakridge, Durban, 4001 &nbsp;|&nbsp; PO Box 72948, Kelvale, 4062</div>

  <svg class="footer-rule" viewBox="0 0 950 4" preserveAspectRatio="none" aria-hidden="true">
    <defs>
      <linearGradient id="ruleGrad" x1="0" x2="1">
        <stop offset="0" stop-color="var(--rule-dark)"/>
        <stop offset="0.45" stop-color="#6f6c2c"/>
        <stop offset="0.75" stop-color="var(--rule-olive)"/>
        <stop offset="1" stop-color="var(--brand-yellow)"/>
      </linearGradient>
    </defs>
    <rect width="950" height="4" fill="url(#ruleGrad)"/>
  </svg>

  <svg class="footer-mark" viewBox="0 0 56 56" aria-hidden="true">
    <circle cx="28" cy="28" r="27" fill="var(--brand-yellow)"/>
  </svg>

  <div class="footer-contacts">
    <span class="contact">
      <svg viewBox="0 0 10 10"><path d="M2 0.5 L3.6 2.6 L2.8 3.6 C3.4 5 4.8 6.5 6.3 7.2 L7.4 6.4 L9.5 8 L8.4 9.5 C4.5 9.2 0.8 5.5 0.5 1.6 Z"/></svg>
      031 684 9152
    </span>
    <span class="contact">
      <svg viewBox="0 0 10 10"><rect x="2.5" y="0.5" width="5" height="3" /><rect x="0.5" y="3.5" width="9" height="4.5" rx="1"/><rect x="2.5" y="8" width="5" height="1.5"/></svg>
      031 739 4218
    </span>
    <span class="contact">
      <svg viewBox="0 0 10 10"><path d="M0.5 2 H9.5 V8 H0.5 Z M0.5 2 L5 5.5 L9.5 2" stroke="#fff" stroke-width="0.8"/></svg>
      contact@dunholt.co.za
    </span>
    <span class="contact">
      <svg viewBox="0 0 10 10"><circle cx="5" cy="5" r="4.5"/><path d="M0.5 5 H9.5 M5 0.5 C3 3 3 7 5 9.5 M5 0.5 C7 3 7 7 5 9.5" stroke="#fff" stroke-width="0.7" fill="none"/></svg>
      www.dunholt.co.zaz
    </span>
  </div>
</main>
</body>
</html>
```